PTA Sign 24”x60”

We need a design for our PTA sign (24”x60”) that is going next to a table (attached is an image of the sign)

I'd like the color scheme to royal blue in the website below and I've attached a few of our school logos.

It should have the colors and simple PTA logo of this tablecloth https://stores.brimlyshop.com/listings.lasso?c_id=Tablecloths&-session=KI_Clients:4QF2870D551ab7E19RwPLN3A826C

The most important thing is the words pop and is easy to read from far away.

Larkfield PTA

What do we do?
Help at school events
Support our school and students
Organize fundraising events
Have fun together!

Questions? Email PTALarkfield@quellmail.com

Get text updates - Text @larkfieldpta to the number 47326

Parents of Elementary School Students

Education

Sans Serif

• Clear words that pop- easy to read

```html
<!DOCTYPE html>
<html lang="en">
<head>
<meta charset="utf-8">
<title>Larkfield PTA – Roll-up Sign</title>
<link rel="stylesheet" href="https://fonts.googleapis.com/css2?family=Open+Sans:wght@600;700;800&display=swap">
<style>
  :root {
    --navy: #1f2a6b;
    --red: #c4000b;
    --white: #ffffff;
    --sky: #d6f1f6;
    --stage: #e8e8ea;
    --silver-dark: #9a9ca3;
    --silver-light: #f4f4f6;
  }
  * { margin: 0; padding: 0; box-sizing: border-box; }
  html, body { width: 1200px; height: 1200px; overflow: hidden; }
  body {
    background: var(--stage);
    font-family: "Open Sans", Arial, sans-serif;
    position: relative;
  }
  .sign {
    position: absolute;
    left: 370px;
    top: 15px;
    width: 460px;
    height: 1170px;
    overflow: hidden;
  }
  .sign-bands { position: absolute; inset: 0; width: 100%; height: 100%; }
  .sign > .block { position: absolute; left: 0; width: 100%; }

  .school-mark {
    top: 60px;
    display: flex;
    flex-direction: column;
    align-items: center;
    gap: 14px;
  }
  .school-mark .mark-dot {
    width: 150px; height: 150px;
    border-radius: 50%;
    background: var(--navy);
  }
  .school-mark .mark-name {
    font-weight: 700;
    font-size: 40px;
    color: var(--navy);
    line-height: 1;
  }

  .title { text-align: center; font-weight: 700; line-height: 1; letter-spacing: -1px; }
  .title-name { top: 364px; font-size: 76px; color: var(--navy); }
  .title-pta { top: 440px; font-size: 86px; color: var(--red); }

  .mission { top: 615px; padding-left: 54px; color: var(--white); }
  .mission-heading { font-weight: 700; line-height: 1; white-space: nowrap; }
  .mission-heading .lead { font-size: 31px; }
  .mission-heading .big { font-size: 54px; font-weight: 800; letter-spacing: -1px; }
  .mission-heading .accent { color: var(--red); }
  .rule {
    margin-top: 14px;
    width: 56px; height: 7px;
    border-radius: 4px;
    background: linear-gradient(90deg, var(--white) 0 30%, var(--red) 30% 100%);
  }
  .mission-list { list-style: none; margin-top: 22px; }
  .mission-list li {
    font-size: 21px; font-weight: 700; line-height: 35.5px;
    white-space: nowrap;
  }
  .mission-list li::before {
    content: "\203A";
    color: var(--red);
    font-weight: 800;
    font-size: 26px;
    margin-right: 7px;
  }

  .contact { top: 930px; text-align: center; color: var(--white); line-height: 1; }
  .contact-heading { font-size: 41px; font-weight: 800; }
  .contact-email { font-size: 25px; font-weight: 600; margin-top: 14px; }
  .contact-sub { font-size: 31px; font-weight: 800; margin-top: 15px; }
  .contact-line { font-size: 23px; font-weight: 700; margin-top: 9px; }
</style>
</head>
<body>
  <main class="sign" aria-label="Larkfield PTA sign">
    <svg class="sign-bands" viewBox="0 0 478 1215" preserveAspectRatio="none" aria-hidden="true">
      <defs>
        <linearGradient id="skyFade" x1="0" y1="0" x2="0" y2="1">
          <stop offset="0" stop-color="#c9eef4"/>
          <stop offset="0.45" stop-color="#f3fbfd"/>
          <stop offset="1" stop-color="#ffffff"/>
        </linearGradient>
        <linearGradient id="silver" x1="0" y1="0" x2="1" y2="0">
          <stop offset="0" stop-color="#9a9ca3"/>
          <stop offset="0.45" stop-color="#f4f4f6"/>
          <stop offset="0.7" stop-color="#c9cacf"/>
          <stop offset="1" stop-color="#f4f4f6"/>
        </linearGradient>
      </defs>
      <rect width="478" height="1215" fill="url(#skyFade)"/>
      <path d="M0,515 Q230,650 478,545 L478,1215 L0,1215Z" fill="#c4000b"/>
      <path d="M0,560 Q240,650 478,553 L478,1215 L0,1215Z" fill="url(#silver)"/>
      <path d="M0,583 Q240,668 478,562 L478,1215 L0,1215Z" fill="#1f2a6b"/>
      <path d="M0,915 Q280,962 478,845 L478,1215 L0,1215Z" fill="url(#silver)"/>
      <path d="M0,928 Q280,978 478,893 L478,1215 L0,1215Z" fill="#c4000b"/>
    </svg>

    <div class="block school-mark">
      <span class="mark-dot"></span>
      <span class="mark-name">Larkfield</span>
    </div>

    <h1 class="block title title-name">Larkfield</h1>
    <div class="block title title-pta">PTA</div>

    <section class="block mission">
      <h2 class="mission-heading">
        <span class="lead">What do</span>
        <span class="big">WE</span>
        <span class="big accent">DO?</span>
      </h2>
      <div class="rule"></div>
      <ul class="mission-list">
        <li>Help at school events</li>
        <li>Support our school and students</li>
        <li>Organize fundraising events</li>
        <li>Have fun together!</li>
      </ul>
    </section>

    <section class="block contact">
      <h2 class="contact-heading">Questions?</h2>
      <p class="contact-email">PTALarkfield@quellmail.com</p>
      <p class="contact-sub">Get text updates</p>
      <p class="contact-line">Text @larkfieldpta</p>
      <p class="contact-line">to the number 47326</p>
    </section>
  </main>
</body>
</html>
```